Business Card Design for new social media business

I am looking for a new professional business card design for an exciting new company which is based on providing members with experiences of others to benefit their choice of places to visit for restaurants, bars, clubs, national monument, tourist sights, hotels and so forth.
Updates

Please submit designs as I will choose to commit the funds depending on designs.

Target Market(s)

Business Managers as well as directors alongside owners

Industry/Entity Type

Business

Requirements
Must have
• Logo design and symbols
Nice to have
• Logo / Symbol on the back of the business card and possibly the logo as if embedded/embossed on the business card.

```html
<!DOCTYPE html>
<html lang="en">
<head>
<meta charset="utf-8">
<title>Tarvessa Business Cards</title>
<link rel="stylesheet" href="https://fonts.googleapis.com/css2?family=Josefin+Sans:wght@400;700&display=swap">
<style>
  :root {
    --backdrop: #e8e5e0;
    --card: #ffffff;
    --brand-blue: #2f5fb3;
    --text-blue: #1f7cc4;
    --accent-orange: #f07a1f;
    --band-blue: #0a84cc;
    --band-orange: #f5a020;
    --faint-mark: rgba(120, 140, 220, 0.12);
  }
  * { margin: 0; padding: 0; box-sizing: border-box; }
  html, body {
    width: 1200px; height: 1000px; overflow: hidden;
    background: var(--backdrop);
    font-family: "Josefin Sans", sans-serif;
  }
  .card {
    position: absolute; width: 545px; height: 315px;
    background: var(--card); overflow: hidden;
    box-shadow: 0 2px 6px rgba(0,0,0,0.15);
  }
  .card--front { left: 36px; top: 34px; }
  .card--back-a { left: 612px; top: 34px; }
  .card--back-b { left: 612px; top: 378px; }

  .wordmark {
    position: absolute; display: flex; align-items: center;
    color: var(--brand-blue); font-weight: 700; letter-spacing: -0.5px;
    white-space: nowrap;
  }
  .wordmark__dot { border-radius: 50%; background: var(--accent-orange); margin-right: 14px; flex: none; }

  .card--front .wordmark { left: 96px; top: 112px; font-size: 64px; }
  .card--front .wordmark__dot { width: 72px; height: 72px; }
  .front-url {
    position: absolute; left: 278px; top: 184px;
    font-size: 9px; letter-spacing: 3px; color: var(--accent-orange); font-weight: 700;
  }

  .card--back-a .wordmark, .card--back-b .wordmark { left: 26px; top: 36px; font-size: 38px; }
  .card--back-a .wordmark__dot, .card--back-b .wordmark__dot { width: 40px; height: 40px; margin-right: 10px; }

  .faint-mark { position: absolute; border-radius: 50%; background: var(--faint-mark); }
  .card--front .faint-mark { width: 150px; height: 150px; right: -40px; bottom: -40px; }
  .card--back-a .faint-mark { width: 210px; height: 210px; right: -10px; top: 20px; }

  .person__name { font-size: 17px; letter-spacing: 2px; color: var(--text-blue); white-space: nowrap; }
  .person__role { font-size: 9px; letter-spacing: 1px; color: var(--accent-orange); }
  .contact { position: absolute; font-size: 11px; line-height: 13px; letter-spacing: 1.5px; color: var(--text-blue); white-space: nowrap; }

  .card--back-a .person { position: absolute; left: 57px; top: 203px; }
  .card--back-a .contact--details { left: 71px; top: 242px; }
  .card--back-a .contact--address { left: 383px; top: 242px; }

  .card--back-b .contact--address { left: 64px; top: 119px; }
  .card--back-b .contact--details { right: 63px; top: 119px; text-align: right; }
  .name-band {
    position: absolute; left: 0; top: 194px; width: 100%; height: 55px;
    background: var(--band-blue); border-bottom: 6px solid var(--band-orange);
    padding: 8px 0 0 47px;
  }
  .name-band .person__name { color: #ffffff; }
  .name-band .person__role { color: #dbeaf7; }
</style>
</head>
<body>
  <section class="card card--front">
    <div class="wordmark"><span class="wordmark__dot"></span>Tarvessa</div>
    <div class="front-url">WWW.TARVESSA.NET</div>
    <div class="faint-mark"></div>
  </section>

  <section class="card card--back-a">
    <div class="wordmark"><span class="wordmark__dot"></span>Tarvessa</div>
    <div class="faint-mark"></div>
    <div class="person">
      <div class="person__name">Maren Castell</div>
      <div class="person__role">Director</div>
    </div>
    <div class="contact contact--details">+38 412 907<br>maren@tarvessa.net<br>www.tarvessa.net</div>
    <div class="contact contact--address">Company address<br>State/town<br>Country</div>
  </section>

  <section class="card card--back-b">
    <div class="wordmark"><span class="wordmark__dot"></span>Tarvessa</div>
    <div class="contact contact--address">Company address<br>State/town<br>Country</div>
    <div class="contact contact--details">+38 412 907<br>maren@tarvessa.net<br>www.tarvessa.net</div>
    <div class="name-band">
      <div class="person__name">Maren Castell</div>
      <div class="person__role">Director</div>
    </div>
  </section>
</body>
</html>
```